Greek Yogurt Design

Design Brief – Premium Greek Yogurt Line (150g Pot)
Background
We are a small-to-medium dairy producer launching a new premium Greek yogurt range. This line will come in slightly larger pots than our standard yogurts, and we are targeting an upmarket clientele with a higher price point.
Product Details
Product: Greek Yogurt (fruit on the bottom, yogurt on top)
Flavours:
Natural
Strawberry
Forest Fruit
Peach & Apricot
Vanilla
Mango
Weight: 150g
Kosher Certification: 2 logos must be applied neatly (logos provided).
Lid: Standard universal lid (not flavour-specific).
Design Style
Clean, elegant, and premium feel (avoid clutter).
Should stand out as sophisticated compared to our standard range.
Visual hierarchy:
Brand & product type (Greek Yogurt) should be clear.
Flavour indicated with subtle but distinct cues (colour palette, fruit illustration/photography).
“Fruit on the bottom” message should be communicated simply.
Premium cues: minimalist typography, restrained colour palette, elegant fruit imagery.
References / Inspiration
Velloran Yogurt
– clean, bold, dairy-traditional.
Bracken Hollow Greek Style
– natural, elegant design.
Lumerra Greek Yogurt
– modern, colourful yet clean.
Deliverables
Pot sleeve / pot design (to wrap around container).
Must work across all flavours with colour/flavour variation.
Space for universal lid (do not design individual lids).
Application of 2 kosher logos in a balanced way.
Updates
Industry/Entity Type
Dairy
Colors
Designer to choose colors to be used in the design.
Look and feel
Each slider illustrates characteristics of the customer's brand and the style your logo design should communicate.

```html
<!DOCTYPE html>
<html lang="en">
<head>
<meta charset="utf-8">
<title>Greek Yogurt – Pot Sleeves</title>
<link href="https://fonts.googleapis.com/css2?family=Kaushan+Script&family=Michroma&display=swap" rel="stylesheet">
<style>
  :root {
    --backdrop: #959493;
    --sleeve-white: #fbfbfb;
    --ink: #1c1c1c;
    --brand-green: #5cb83a;
    --strawberry: #d6127c;
    --strawberry-soft: #f1b8d3;
    --peach: #d9362b;
    --peach-soft: #f3c3b5;
    --badge-line: #8a8a8a;
  }
  * { box-sizing: border-box; margin: 0; padding: 0; }
  html, body { width: 1200px; height: 735px; overflow: hidden; }
  body {
    background: var(--backdrop);
    position: relative;
    font-family: "Michroma", sans-serif;
  }
  .sleeve {
    position: absolute;
    top: 225px;
    width: 500px;
    height: 330px;
    background: var(--sleeve-white);
    overflow: hidden;
    border-radius: 4px;
  }
  .sleeve--strawberry { left: 80px; --flavour: var(--strawberry); --flavour-soft: var(--strawberry-soft); }
  .sleeve--peach { left: 620px; --flavour: var(--peach); --flavour-soft: var(--peach-soft); }

  .sleeve__top-band {
    position: absolute; left: 0; top: 0; width: 100%; height: 110px;
    background: var(--flavour);
  }
  .sleeve__top-band svg { position: absolute; bottom: -1px; left: 0; }
  .sleeve__bottom-band {
    position: absolute; left: 0; bottom: 0; width: 100%; height: 34px;
    background: var(--flavour);
  }
  .sleeve__bottom-band svg { position: absolute; top: -1px; left: 0; }

  .brand-tag {
    position: absolute; left: 50%; top: 92px; transform: translateX(-50%);
    width: 124px; height: 46px; border-radius: 24px;
    background: var(--sleeve-white);
    border: 3px solid var(--flavour);
    display: flex; align-items: center; justify-content: center;
  }
  .brand-tag__name {
    font-size: 14px; line-height: 1; color: var(--brand-green); letter-spacing: 0.5px;
  }

  .product-title {
    position: absolute; left: 22px; top: 140px;
    font-family: "Kaushan Script", cursive;
    font-size: 58px; line-height: 1; font-weight: 400; color: var(--ink);
    white-space: nowrap;
  }
  .flavour-name {
    position: absolute; left: 52px; top: 208px;
    font-size: 13px; line-height: 16px; color: var(--flavour); letter-spacing: 2px;
    text-transform: uppercase; white-space: nowrap;
  }
  .fruit-note {
    position: absolute; left: 52px; top: 228px;
    font-size: 11px; line-height: 14px; color: var(--flavour); letter-spacing: 1.5px;
    text-transform: uppercase; white-space: nowrap;
  }
  .fruit-visual {
    position: absolute; right: 30px; top: 216px;
    width: 200px; height: 70px; border-radius: 50%;
  }
  .sleeve--strawberry .fruit-visual {
    background: radial-gradient(ellipse at 50% 45%, #c8262e 0 28%, #f6d3e3 40%, rgba(255,255,255,0) 70%);
  }
  .sleeve--peach .fruit-visual {
    background: radial-gradient(ellipse at 50% 45%, #f0a040 0 28%, #f7d7cc 40%, rgba(255,255,255,0) 70%);
  }
  .certifications {
    position: absolute; left: 30px; top: 260px;
    display: flex; gap: 8px; align-items: flex-start;
  }
  .cert-mark {
    width: 22px; height: 22px; border-radius: 50%;
    border: 1.5px solid var(--badge-line); background: #f0f0f0;
  }
  .cert-mark--green { border-color: var(--brand-green); }
  .cert-caption {
    position: absolute; left: 30px; top: 284px;
    font-size: 5px; line-height: 6px; color: #555; letter-spacing: 0.5px; text-transform: uppercase;
  }
  .net-weight {
    position: absolute; left: 110px; top: 270px;
    font-size: 11px; line-height: 14px; color: var(--ink); letter-spacing: 2px;
  }
</style>
</head>
<body>

<section class="sleeve sleeve--strawberry">
  <div class="sleeve__top-band">
    <svg width="500" height="30" viewBox="0 0 500 30" preserveAspectRatio="none"><path d="M0 30 L0 22 Q250 0 500 8 L500 30 Z" fill="#fbfbfb"/></svg>
  </div>
  <div class="brand-tag"><span class="brand-tag__name">Orlenna</span></div>
  <h1 class="product-title">Greek Yogurt</h1>
  <p class="flavour-name">Strawberry</p>
  <p class="fruit-note">Fruit on<br>the bottom</p>
  <div class="fruit-visual" role="img" aria-label="Fresh strawberries resting on a swirl of pink yogurt"></div>
  <div class="certifications">
    <span class="cert-mark"></span>
    <span class="cert-mark cert-mark--green"></span>
  </div>
  <p class="cert-caption">Kosher dairy</p>
  <p class="net-weight">150G</p>
  <div class="sleeve__bottom-band">
    <svg width="500" height="14" viewBox="0 0 500 14" preserveAspectRatio="none"><path d="M0 0 L500 0 L500 2 Q250 14 0 6 Z" fill="#fbfbfb"/></svg>
  </div>
</section>

<section class="sleeve sleeve--peach">
  <div class="sleeve__top-band">
    <svg width="500" height="30" viewBox="0 0 500 30" preserveAspectRatio="none"><path d="M0 30 L0 22 Q250 0 500 8 L500 30 Z" fill="#fbfbfb"/></svg>
  </div>
  <div class="brand-tag"><span class="brand-tag__name">Orlenna</span></div>
  <h1 class="product-title">Greek Yogurt</h1>
  <p class="flavour-name">Peach &amp; Apricot</p>
  <p class="fruit-note">Fruit on<br>the bottom</p>
  <div class="fruit-visual" role="img" aria-label="Whole peach and halved apricot with leaves on a swirl of yogurt"></div>
  <div class="certifications">
    <span class="cert-mark"></span>
    <span class="cert-mark cert-mark--green"></span>
  </div>
  <p class="cert-caption">Kosher dairy</p>
  <p class="net-weight">150G</p>
  <div class="sleeve__bottom-band">
    <svg width="500" height="14" viewBox="0 0 500 14" preserveAspectRatio="none"><path d="M0 0 L500 0 L500 2 Q250 14 0 6 Z" fill="#fbfbfb"/></svg>
  </div>
</section>

</body>
</html>
```